Capability Statement Brochure - Corporate

We need to provide our corporate clients with an elegant, professional and well designed capability statement that not only details what our business can offer, but reflects our professionalism with relevant technical photos. I am thinking two pages A 4 pdf will be suitable if the text can fit without looking crowded but happy to extend to 3 or 4 pages if needed . Colours and details can be taken from our website www.quorintech.com.au Some photos have been attached however if we need more professional stock photos I am happy to use them if needed. This project needs to convince potential clients we are the best in industry and our capability is extensive. Please help us relay this to our customers. Thank you,.

Target Market(s)

Corporate, Government, Education, Defence, Healthcare

Industry/Entity Type

Audio Visual Integration

Colors
0054AA
0677BA
7BADD7
CADEEF
E8F1F8

Requirements
Must have
• Style, look classy, sophisticated and technical
Nice to have
• Quorin Tech colours, Logo, website and email and include the PRISM LED Logo
Should not have
• Messy, too much clutter, not easy to read.

```html
<!DOCTYPE html>
<html lang="en">
<head>
<meta charset="utf-8">
<title>Quorin Tech – Capability Statement</title>
<link href="https://fonts.googleapis.com/css2?family=Poppins:wght@400;500;600;700;800&display=swap" rel="stylesheet">
<style>
:root{
  --navy:#111c36;
  --blue:#0054AA;
  --mid:#0677BA;
  --sky:#7BADD7;
  --pale:#CADEEF;
  --mist:#E8F1F8;
  --orange:#e8621d;
  --ink:#2a3345;
  --bg:#e7e5e3;
  --white:#ffffff;
}
*{box-sizing:border-box;margin:0;padding:0}
html,body{width:1200px;height:1200px;overflow:hidden;background:var(--bg);font-family:"Poppins",sans-serif;color:var(--ink)}
.page{position:absolute;top:232px;width:520px;height:736px;background:var(--white);box-shadow:0 6px 22px rgba(0,0,0,.12);overflow:hidden}
.page--one{left:60px}
.page--two{left:620px}

.masthead{height:58px;display:flex;justify-content:space-between;align-items:center;padding:0 18px;border-bottom:2px solid var(--orange)}
.brand{display:flex;align-items:center;gap:8px}
.brand__mark{width:24px;height:24px;background:var(--blue)}
.brand__name{font-size:15px;font-weight:600;color:var(--blue);line-height:1}
.contact{text-align:right;font-size:7px;line-height:1.5;color:var(--mid)}
.contact__phone{font-weight:700;font-size:8.5px;color:var(--blue)}
.contact__title{font-weight:700;font-size:8.5px;color:var(--blue)}

.hero{position:relative;height:138px;background:linear-gradient(120deg,#1b4f92 0%,#2e6cb0 45%,#6c95c4 100%);border-bottom:3px solid var(--orange);padding:22px 18px}
.hero__title{font-size:22px;font-weight:700;color:var(--white);letter-spacing:.3px}
.hero__sub{font-size:10px;color:var(--orange);font-weight:500;margin-top:2px}
.hero__list{font-size:7.5px;color:var(--white);margin-top:6px}
.hero__badge{position:absolute;right:18px;top:52px;width:82px;background:var(--orange);color:var(--white);text-align:center;padding:6px 4px;border-radius:2px}
.hero__badge b{display:block;font-size:10px;font-weight:700}
.hero__badge span{font-size:5.5px;text-transform:uppercase}

.body{display:grid;grid-template-columns:1fr 1fr;gap:10px;padding:10px 14px 0}
.section-title{font-size:8.5px;font-weight:700;color:var(--blue);text-transform:uppercase;border-bottom:1.5px solid var(--orange);padding-bottom:2px;margin:6px 0 6px}
.section-title:first-child{margin-top:0}
.copy{font-size:6.8px;line-height:1.55;margin-bottom:5px}

.points{display:flex;flex-direction:column;gap:5px}
.point{display:flex;gap:6px;background:var(--mist);border-left:2.5px solid var(--blue);padding:5px 6px}
.icon{flex:none;width:12px;height:12px}
.point__title{font-size:7.2px;font-weight:700;color:var(--blue)}
.point__text{font-size:6.2px;line-height:1.45}

.photo{position:relative}
.photo--boardroom{height:150px;margin-top:8px;background:linear-gradient(170deg,#d8e3ee,#8ea5bf 55%,#3c4d66)}
.photo--classroom{height:238px;background:linear-gradient(175deg,#e9e6de,#b5b0a4 50%,#4a4a4e)}
.photo--mixer{height:280px;margin-top:8px;background:linear-gradient(150deg,#5a6470,#22272e 50%,#0c0f14)}
.photo--office{height:124px;background:linear-gradient(175deg,#f1f3f5,#c9cfd6 60%,#8c9299)}
.caption{position:absolute;left:0;right:0;bottom:0;background:var(--blue);color:var(--white);font-size:6.5px;font-weight:500;padding:3px 5px}

.services{display:grid;grid-template-columns:1fr 1fr;gap:5px}
.service{background:var(--mist)}
.service__head{background:var(--blue);color:var(--white);font-size:6.8px;font-weight:600;padding:4px 6px;display:flex;align-items:center;gap:4px}
.service ul{list-style:none;padding:4px 6px 5px}
.service li{font-size:6.1px;line-height:1.6;position:relative;padding-left:7px}
.service li::before{content:"";position:absolute;left:0;top:4px;width:3px;height:3px;border-radius:50%;background:var(--orange)}

.sectors{display:grid;grid-template-columns:repeat(4,1fr);gap:3px;margin-bottom:8px}
.sector{background:var(--mid);color:var(--white);font-size:5.5px;line-height:1.3;text-align:center;padding:3px 2px;height:21px;display:flex;align-items:center;justify-content:center}

.footer{position:absolute;left:0;right:0;bottom:0;height:40px;background:var(--navy);padding:8px 16px 0;color:var(--white)}
.footer__row{display:flex;justify-content:space-between;font-size:6.5px}
.footer__cta{color:var(--orange);font-weight:700}
.footer__page{text-align:center;font-size:5.5px;color:var(--sky);margin-top:7px}

.checks{list-style:none}
.checks li{font-size:6.6px;line-height:1.62;position:relative;padding-left:12px}
.checks li::before{content:"";position:absolute;left:0;top:2px;width:8px;height:8px;background:var(--blue);border-radius:1px}
.checks li::after{content:"";position:absolute;left:2.8px;top:3.2px;width:2px;height:4px;border:solid var(--white);border-width:0 1.2px 1.2px 0;transform:rotate(45deg)}

.steps{display:flex;flex-direction:column;gap:5px}
.step{display:flex;gap:8px;align-items:center;background:var(--mist);border-left:2.5px solid var(--blue);padding:6px 7px}
.step__title{font-size:7px;font-weight:700;color:var(--blue)}
.step__text{font-size:6px;line-height:1.45}

.offices{display:grid;grid-template-columns:1fr 1fr;gap:4px;margin-bottom:6px}
.office{background:var(--mist)}
.office__head{background:var(--blue);color:var(--white);font-size:6.6px;font-weight:600;padding:3px 6px;display:flex;align-items:center;gap:4px}
.office__body{display:flex;justify-content:space-between;align-items:center;gap:4px;padding:3px 6px;font-size:5.4px;line-height:1.35}
.office__phone{font-size:7px;font-weight:700;color:var(--blue);white-space:nowrap}

.product-band{position:absolute;left:0;right:0;bottom:40px;height:72px;background:var(--navy);display:flex;align-items:center;justify-content:space-between;padding:0 16px;color:var(--white);border-bottom:1px solid #2a3553}
.band__label{font-size:6px;font-weight:700;color:var(--orange);text-transform:uppercase;margin-bottom:2px}
.band__text{font-size:6px;line-height:1.45;width:130px}
.band__right{text-align:right}
.band__right .band__text{margin-left:auto}
.product-tile{background:var(--white);width:104px;height:40px;border-radius:2px;display:flex;align-items:center;justify-content:center;gap:5px}
.product-tile__dot{width:7px;height:7px;background:var(--navy)}
.product-tile__name{font-size:11px;font-weight:700;color:var(--navy)}
</style>
</head>
<body>

<section class="page page--one">
  <header class="masthead">
    <div class="brand">
      <div class="brand__mark"></div>
      <div class="brand__name">quorin tech</div>
    </div>
    <div class="contact">
      <div class="contact__phone">1300 555 210</div>
      <div>www.quorintech.com.au</div>
      <div>info@quorintech.com.au</div>
    </div>
  </header>

  <div class="hero" role="img" aria-label="Lecture theatre with audio visual displays">
    <h1 class="hero__title">CAPABILITY STATEMENT</h1>
    <p class="hero__sub">Professional Audio Visual Integration</p>
    <p class="hero__list">Design · Supply · Installation · Service &amp; Support</p>
    <div class="hero__badge"><b>24+ YEARS</b><span>of excellence</span></div>
  </div>

  <div class="body">
    <div>
      <h2 class="section-title">Company Overview</h2>
      <p class="copy">Quorin Tech Systems is Australia's leading professional audio visual systems integrator. With over 24 years of industry leadership, we design, deliver and support world-class AV, communications and collaboration technology — connecting people with technology every day.</p>
      <p class="copy">Established in Melbourne in 2000, we operate from offices in Victoria, New South Wales, Queensland and Western Australia, delivering national coverage with genuine local expertise.</p>

      <h2 class="section-title">Our Points of Difference</h2>
      <div class="points">
        <div class="point">
          <svg class="icon" viewBox="0 0 12 12"><path d="M6 1v10M1 6h10M2.5 2.5l7 7M9.5 2.5l-7 7" stroke="#0054AA" stroke-width="1.2"/></svg>
          <div><div class="point__title">Complete Customisation</div><div class="point__text">Bespoke AV solutions tailored to any budget, timeline or unique requirement.</div></div>
        </div>
        <div class="point">
          <svg class="icon" viewBox="0 0 12 12"><circle cx="4" cy="4" r="2" fill="#0054AA"/><circle cx="8.5" cy="4" r="2" fill="#0677BA"/><path d="M0.5 10.5c0-3 7-3 7 0M5 10.5c0-3 7-3 7 0" stroke="#0054AA" fill="none"/></svg>
          <div><div class="point__title">Industry Experience</div><div class="point__text">24+ years of landmark projects across heritage buildings, hospitals and defence facilities.</div></div>
        </div>
        <div class="point">
          <svg class="icon" viewBox="0 0 12 12"><path d="M7 0.5L2.5 7H6l-1 4.5L9.5 5H6z" fill="#0054AA"/></svg>
          <div><div class="point__title">Turnkey Solutions</div><div class="point__text">From concept design to final commissioning — one accountable delivery partner.</div></div>
        </div>
        <div class="point">
          <svg class="icon" viewBox="0 0 12 12"><circle cx="6" cy="6" r="3.2" stroke="#0054AA" stroke-width="1.6" fill="none" stroke-dasharray="2 1.2"/><circle cx="6" cy="6" r="1.2" fill="#0054AA"/></svg>
          <div><div class="point__title">R&amp;D Partnerships</div><div class="point__text">Deep alliances with world-leading AV manufacturers keep us at the forefront.</div></div>
        </div>
      </div>
      <div class="photo photo--boardroom" role="img" aria-label="Corporate boardroom with conference table and display"></div>
    </div>

    <div>
      <h2 class="section-title">Core Services</h2>
      <div class="services">
        <div class="service">
          <div class="service__head"><svg width="8" height="7" viewBox="0 0 8 7"><rect x=".5" y=".5" width="7" height="4.5" fill="none" stroke="#fff"/><path d="M2.5 6.5h3" stroke="#fff"/></svg>Visual Solutions</div>
          <ul><li>PRISM LED Video Walls</li><li>Interactive Touchscreens</li><li>LCD Multi-Screen Walls</li><li>Data Projection Systems</li></ul>
        </div>
        <div class="service">
          <div class="service__head"><svg width="7" height="7" viewBox="0 0 7 7"><rect x="1" y=".5" width="5" height="6" fill="none" stroke="#fff"/><circle cx="3.5" cy="4.2" r="1.1" fill="#fff"/></svg>Audio Solutions</div>
          <ul><li>Paging &amp; Public Address</li><li>Bkgd Music &amp; Live Audio</li><li>Multizone Distribution</li><li>Conferencing Audio &amp; DSP</li></ul>
        </div>
        <div class="service">
          <div class="service__head"><svg width="8" height="6" viewBox="0 0 8 6"><rect x=".5" y=".5" width="5" height="5" fill="none" stroke="#fff"/><path d="M5.5 3l2-1.5v3z" fill="#fff"/></svg>Video Conferencing</div>
          <ul><li>Zentra Rooms &amp; Teamlink</li><li>Ciraq Meet &amp; Polyvox</li><li>Boardroom Systems</li><li>Hybrid Platforms</li></ul>
        </div>
        <div class="service">
          <div class="service__head"><svg width="7" height="7" viewBox="0 0 7 7"><circle cx="3.5" cy="3.5" r="3" fill="none" stroke="#fff"/><path d="M.5 3.5h6M3.5.5v6" stroke="#fff" stroke-width=".7"/></svg>Control &amp; IPTV</div>
          <ul><li>Corvane / Altrix / Extavo</li><li>Smart Building Control</li><li>IPTV &amp; Free-to-Air</li><li>Room Booking Systems</li></ul>
        </div>
      </div>

      <h2 class="section-title">Sectors We Serve</h2>
      <div class="sectors">
        <div class="sector">Corporate &amp; Government</div>
        <div class="sector">Defence &amp; Aerospace</div>
        <div class="sector">Education &amp; TAFE</div>
        <div class="sector">Healthcare &amp; Aged Care</div>
        <div class="sector">Hotels &amp; Hospitality</div>
        <div class="sector">Houses of Worship</div>
        <div class="sector">Mining &amp; Resources</div>
        <div class="sector">Shopping Centres</div>
      </div>

      <div class="photo photo--classroom" role="img" aria-label="Computer training room with rows of desks and projector">
        <div class="caption">Education &amp; Training Technology</div>
      </div>
    </div>
  </div>

  <footer class="footer">
    <div class="footer__row"><span>1300 555 210 &nbsp;·&nbsp; www.quorintech.com.au &nbsp;·&nbsp; info@quorintech.com.au</span><span class="footer__cta">CONNECTING PEOPLE WITH TECHNOLOGY</span></div>
    <div class="footer__page">Page 1 of 2</div>
  </footer>
</section>

<section class="page page--two">
  <header class="masthead">
    <div class="brand">
      <div class="brand__mark"></div>
      <div class="brand__name">quorin tech</div>
    </div>
    <div class="contact">
      <div class="contact__title">CAPABILITY STATEMENT 2024</div>
      <div>1300 555 210 &nbsp;·&nbsp; www.quorintech.com.au</div>
    </div>
  </header>

  <div class="body">
    <div>
      <h2 class="section-title">Technical Expertise</h2>
      <ul class="checks">
        <li>Corvane, Altrix &amp; Extavo certified control systems</li>
        <li>AV-over-IP and fibre optic signal distribution</li>
        <li>Teamlink Rooms, Zentra Rooms &amp; Ciraq Meet</li>
        <li>Duralink &amp; Qoris networked audio architecture</li>
        <li>Fine-pitch LED &amp; LCD video wall calibration</li>
        <li>Interactive flat panels &amp; collaborative displays</li>
        <li>IPTV head-end design and content management</li>
        <li>Room booking &amp; occupancy management systems</li>
        <li>Digital signage network and content delivery</li>
        <li>Structured cabling &amp; professional rack builds</li>
      </ul>

      <h2 class="section-title">Why Choose QT</h2>
      <ul class="checks">
        <li>24+ years of Australian AV industry leadership</li>
        <li>National offices: VIC · NSW · QLD · WA</li>
        <li>Certified engineers &amp; factory-trained technicians</li>
        <li>Vendor-agnostic — right solution, always</li>
        <li>SLA-backed service &amp; maintenance programs</li>
        <li>OH&amp;S compliant · COVID-Safe registered</li>
        <li>Sustainability-committed · Ethical supply chain</li>
        <li>ISO Quality Management standards</li>
      </ul>

      <div class="photo photo--mixer" role="img" aria-label="Digital audio mixing console with faders">
        <div class="caption">Professional Audio System Control</div>
      </div>
    </div>

    <div>
      <h2 class="section-title">Service Delivery</h2>
      <div class="steps">
        <div class="step">
          <svg class="icon" viewBox="0 0 12 12"><path d="M7 0.5L2.5 7H6l-1 4.5L9.5 5H6z" fill="#0054AA"/></svg>
          <div><div class="step__title">AV System Design &amp; Specification</div><div class="step__text">Detailed needs analysis, concept design, CAD schematics and full tender documentation — ensuring correct specification from day one.</div></div>
        </div>
        <div class="step">
          <svg class="icon" viewBox="0 0 12 12"><circle cx="6" cy="6" r="3.2" stroke="#0054AA" stroke-width="1.6" fill="none" stroke-dasharray="2 1.2"/><circle cx="6" cy="6" r="1.2" fill="#0054AA"/></svg>
          <div><div class="step__title">Supply &amp; Project Management</div><div class="step__text">End-to-end procurement, project scheduling and dedicated management to keep every project on time and on budget.</div></div>
        </div>
        <div class="step">
          <svg class="icon" viewBox="0 0 12 12"><rect x="1" y="2" width="10" height="8" fill="none" stroke="#0054AA" stroke-width="1.2"/><rect x="3" y="4.5" width="3" height="3" fill="#0054AA"/></svg>
          <div><div class="step__title">Installation &amp; Commissioning</div><div class="step__text">Expert on-site installation by certified technicians, full commissioning, programming, testing and client sign-off.</div></div>
        </div>
        <div class="step">
          <svg class="icon" viewBox="0 0 12 12"><circle cx="4" cy="4" r="2" fill="#0054AA"/><circle cx="8.5" cy="4" r="2" fill="#0677BA"/><path d="M0.5 10.5c0-3 7-3 7 0M5 10.5c0-3 7-3 7 0" stroke="#0054AA" fill="none"/></svg>
          <div><div class="step__title">Training &amp; Handover</div><div class="step__text">Comprehensive user and admin training, custom quick-reference guides and thorough handover documentation.</div></div>
        </div>
        <div class="step">
          <svg class="icon" viewBox="0 0 12 12"><path d="M2 7V6a4 4 0 0 1 8 0v1" stroke="#0054AA" stroke-width="1.2" fill="none"/><rect x="1.2" y="6.5" width="2" height="3" fill="#0054AA"/><rect x="8.8" y="6.5" width="2" height="3" fill="#0054AA"/></svg>
          <div><div class="step__title">Service &amp; Maintenance</div><div class="step__text">Flexible SLA-backed agreements, preventive maintenance, remote monitoring and rapid on-site support.</div></div>
        </div>
      </div>

      <h2 class="section-title">National Offices</h2>
      <div class="offices">
        <div class="office">
          <div class="office__head"><svg width="6" height="7" viewBox="0 0 6 7"><path d="M3 7S.3 4 .3 2.7a2.7 2.7 0 0 1 5.4 0C5.7 4 3 7 3 7z" fill="#fff"/></svg>Victoria (HQ)</div>
          <div class="office__body"><span>12/40 Harlow Rd,<br>Kelvin Park 3170</span><span class="office__phone">03 9000 1420</span></div>
        </div>
        <div class="office">
          <div class="office__head"><svg width="6" height="7" viewBox="0 0 6 7"><path d="M3 7S.3 4 .3 2.7a2.7 2.7 0 0 1 5.4 0C5.7 4 3 7 3 7z" fill="#fff"/></svg>New South Wales</div>
          <div class="office__body"><span>26/88 Penrose St,<br>Easton 2016</span><span class="office__phone">02 9000 2630</span></div>
        </div>
        <div class="office">
          <div class="office__head"><svg width="6" height="7" viewBox="0 0 6 7"><path d="M3 7S.3 4 .3 2.7a2.7 2.7 0 0 1 5.4 0C5.7 4 3 7 3 7z" fill="#fff"/></svg>Queensland</div>
          <div class="office__body"><span>3/7 Corlan St,<br>Westbrook 4051</span><span class="office__phone">07 3000 4170</span></div>
        </div>
        <div class="office">
          <div class="office__head"><svg width="6" height="7" viewBox="0 0 6 7"><path d="M3 7S.3 4 .3 2.7a2.7 2.7 0 0 1 5.4 0C5.7 4 3 7 3 7z" fill="#fff"/></svg>Western Australia</div>
          <div class="office__body"><span>62 Marden St,<br>Lindell Park 6019</span><span class="office__phone">08 9000 3850</span></div>
        </div>
      </div>

      <div class="photo photo--office" role="img" aria-label="Bright corporate training and meeting room">
        <div class="caption">Corporate Training &amp; Meeting Environments</div>
      </div>
    </div>
  </div>

  <div class="product-band">
    <div>
      <div class="band__label">Signature Product</div>
      <div class="band__text">Fine-pitch modular LED video wall technology — seamless visuals for any venue.</div>
    </div>
    <div class="product-tile"><span class="product-tile__dot"></span><span class="product-tile__name">PRISM LED</span></div>
    <div class="band__right">
      <div class="band__label">Certified &amp; Compliant</div>
      <div class="band__text">ISO Quality Management<br>COVID-Safe Registered · OH&amp;S Compliant</div>
    </div>
  </div>

  <footer class="footer">
    <div class="footer__row"><span>1300 555 210 &nbsp;·&nbsp; www.quorintech.com.au &nbsp;·&nbsp; info@quorintech.com.au</span><span class="footer__cta">CONNECTING PEOPLE WITH TECHNOLOGY</span></div>
    <div class="footer__page">Page 2 of 2</div>
  </footer>
</section>

</body>
</html>
```